Falcrest security business card

Looking for a business card for my security company

Target Market(s)

Security

Industry/Entity Type

Security

Contact Information for Business Card

Name - Gil Marston. Title - General manager - direct 314 862.4490 website www. falcrestsecurityservices.example email - gil@ falcrestsecurityservices.example

Requirements
Must have
• Logo attached

```html
<!DOCTYPE html>
<html lang="en">
<head>
<meta charset="utf-8">
<title>Falcrest Security Services – Business Card</title>
<link href="https://fonts.googleapis.com/css2?family=Montserrat:wght@400;500;700&display=swap" rel="stylesheet">
<style>
  :root {
    --page-bg: #e6e6e6;
    --card-dark: #0c0c0c;
    --card-light: #fbfbfb;
    --gold: #c9a24a;
    --ink: #111111;
    --ink-soft: #2a2a2a;
    --star-tint: #e9e9ec;
  }
  * { margin: 0; padding: 0; box-sizing: border-box; }
  html, body {
    width: 1200px; height: 800px; overflow: hidden;
    background: var(--page-bg);
    font-family: "Montserrat", sans-serif;
  }
  .canvas {
    position: relative; width: 1200px; height: 800px;
  }
  .card {
    position: absolute; top: 257px;
    width: 500px; height: 286px;
    box-shadow: 0 10px 30px rgba(0,0,0,0.18);
    overflow: hidden;
  }
  /* Front side */
  .card--front { left: 70px; background: var(--card-dark); }
  .front__rule {
    position: absolute; top: 142px; height: 1px; background: var(--gold);
  }
  .front__rule--left { left: 0; width: 150px; }
  .front__rule--right { right: 0; width: 150px; }
  .front__brand {
    position: absolute; left: 150px; width: 200px; top: 122px;
    display: flex; align-items: center; justify-content: center; gap: 8px;
  }
  .front__brand-dot {
    width: 12px; height: 12px; border-radius: 50%; background: var(--gold);
  }
  .front__brand-name {
    font-weight: 700; font-size: 32px; line-height: 40px;
    letter-spacing: 1px; color: var(--gold); text-transform: uppercase;
  }
  .front__web {
    position: absolute; left: 0; right: 0; top: 222px; text-align: center;
    font-size: 13px; letter-spacing: 3.2px; color: var(--gold);
  }
  /* Back side */
  .card--back { left: 630px; background: var(--card-light); }
  .back__stars {
    position: absolute; top: 0; height: 286px;
    background: radial-gradient(ellipse at center, var(--star-tint) 0%, rgba(233,233,236,0) 70%);
  }
  .back__stars--left { left: 0; width: 120px; }
  .back__stars--right { right: 0; width: 130px; }
  .back__rule {
    position: absolute; top: 150px; height: 1.5px; background: var(--ink);
  }
  .back__rule--left { left: 0; width: 200px; }
  .back__rule--right { left: 340px; right: 0; }
  .back__brand {
    position: absolute; left: 100px; top: 88px;
    font-weight: 700; font-size: 34px; line-height: 40px;
    letter-spacing: 1px; color: var(--ink); text-transform: uppercase;
  }
  .back__person {
    position: absolute; left: 200px; top: 130px; width: 140px; height: 42px;
    border: 1.5px solid var(--ink); background: var(--card-light);
    display: flex; flex-direction: column; justify-content: center;
    padding-left: 10px;
  }
  .person__name {
    font-size: 15px; line-height: 17px; color: var(--ink); font-weight: 400;
  }
  .person__name strong { font-weight: 700; }
  .person__title { font-size: 10px; line-height: 12px; color: var(--ink-soft); }
  .back__contact {
    position: absolute; left: 0; right: 0; top: 192px;
    display: flex; flex-direction: column; align-items: center; gap: 10px;
    font-size: 11px; color: var(--ink);
  }
  .contact__row { display: flex; align-items: center; gap: 6px; }
  .contact__icon { width: 10px; height: 10px; }
</style>
</head>
<body>
<main class="canvas">
  <section class="card card--front" aria-label="Card front">
    <div class="front__rule front__rule--left"></div>
    <div class="front__rule front__rule--right"></div>
    <div class="front__brand">
      <span class="front__brand-dot"></span>
      <span class="front__brand-name">Falcrest</span>
    </div>
    <p class="front__web">www. falcrestsecurityservices.example</p>
  </section>

  <section class="card card--back" aria-label="Card back">
    <div class="back__stars back__stars--left" role="img" aria-label="Scattered faint grey stars"></div>
    <div class="back__stars back__stars--right" role="img" aria-label="Scattered faint grey stars"></div>
    <div class="back__rule back__rule--left"></div>
    <div class="back__rule back__rule--right"></div>
    <p class="back__brand">Falcrest</p>
    <div class="back__person">
      <p class="person__name"><strong>Gil</strong> Marston</p>
      <p class="person__title">General manager</p>
    </div>
    <div class="back__contact">
      <p class="contact__row">
        <svg class="contact__icon" viewBox="0 0 10 10" aria-hidden="true"><circle cx="5" cy="5" r="5" fill="#111"/><path d="M3.2 2.6c.3-.3.6-.2.8.1l.4.7c.1.2 0 .4-.2.6l-.2.2c.3.6.8 1.1 1.4 1.4l.2-.2c.2-.2.4-.3.6-.2l.7.4c.3.2.4.5.1.8-.4.5-1 .6-1.6.3C4.3 6.1 3.5 5.3 3 4.3c-.3-.6-.2-1.2.2-1.7z" fill="#fff"/></svg>
        314 862.4490
      </p>
      <p class="contact__row">gil@ falcrestsecurityservices.example</p>
    </div>
  </section>
</main>
</body>
</html>
```